The Dwelling Journal - Double Truck Ad

BACKGROUND:
Brightfold Retractable Shades was started in 1997 by husband and wife team Gareth and Wendy Trovaldi. Since then we have expanded to not only local sales in Southern Arizona, but to a dealer network that spans the United States allowing them to serve homeowners, businesses and government agencies from Alaska to Hawaii.
PROJECT BRIEF:
We advertise monthly in The Dwelling Journal Tucson and are in need of a new, refreshed 2 page (double truck) spread. We want to show off the products we offer in a professional, but eye-catching way. Our clientele are usually older, upper middle class - upper class and are now retired so they want to enjoy their home more.
The ad should be easy to follow and achieve the end goal of making the reader pick up the phone to schedule an estimate appointment with us. It should convey that amongst our competitors, we are the superior choice. I have attached ads we have done in the past for your reference. It is preferred that the winner submit an InDesign file format, but not required.
REQUIRED TEXT:
Locally Manufactured in Tucson for Over 25 Years
520.555.0187
Visit our showroom
473 W. Pellham Rd | Tucson, AZ 85790 | Mon - Fri 10a - 4p
www.brightfoldcovers.example
Bonded • Insured ROC# CR-904317
20% off - Some exclusions may apply. Cannot be combined with other offers or discounts. Expires 8/18/22
SIZE: Flat (finished): 16.5" W x 11" H - with 0.25" margins and a 0.125" bleed

```html
<!DOCTYPE html>
<html lang="en">
<head>
<meta charset="utf-8">
<title>Brightfold Retractable Shades – Double Truck Ad</title>
<link href="https://fonts.googleapis.com/css2?family=Montserrat:wght@500;600;700;800;900&family=Oswald:wght@600;700&display=swap" rel="stylesheet">
<style>
  :root{
    --navy:#0f4a86;
    --navy-deep:#0b3c70;
    --mid-blue:#3f7cc0;
    --sky-blue:#5b95d3;
    --yellow:#f0d445;
    --ink:#1c1c1c;
    --paper:#ffffff;
    --backdrop:#e6e6e6;
    --rule:#7a7a7a;
  }
  *{box-sizing:border-box;margin:0;padding:0}
  html,body{width:800px;height:1200px;overflow:hidden;background:var(--backdrop)}
  body{position:relative;font-family:"Montserrat",Arial,sans-serif;color:var(--ink)}
  .ad{position:absolute;left:20px;top:346px;width:760px;height:507px;background:var(--paper);overflow:hidden;box-shadow:0 8px 20px rgba(0,0,0,.18)}
  .hero{position:absolute;left:0;top:0;width:760px;height:255px;background:var(--navy);overflow:hidden}
  .hero-photo{position:absolute;left:300px;top:0;width:460px;height:255px;
    background:linear-gradient(180deg,#8fb6e4 0%,#b9d0ea 22%,#c8b79a 40%,#7d9a5d 62%,#b98f6c 80%,#a57a5a 100%)}
  .hero-fade{position:absolute;left:0;top:0;width:760px;height:255px;
    background:linear-gradient(90deg,var(--navy) 0%,var(--navy) 40%,rgba(15,74,134,.55) 52%,rgba(15,74,134,0) 66%)}
  .hero-waves{position:absolute;left:0;top:0}
  .brand{position:absolute;left:34px;top:24px;display:flex;align-items:center;gap:8px}
  .brand-dot{width:34px;height:34px;border-radius:50%;background:var(--mid-blue);border:2px solid #fff}
  .brand-name{font-weight:700;font-size:17px;color:#fff;letter-spacing:.5px}
  .headline{position:absolute;left:34px;top:76px;line-height:1}
  .headline-main{display:block;font-weight:900;font-size:34px;color:var(--yellow);letter-spacing:-.5px}
  .headline-sub{display:block;font-weight:800;font-size:21.5px;color:#fff;margin-top:5px;letter-spacing:-.2px}
  .headline-bar{position:absolute;left:55px;top:144px;width:36px;height:3px;background:var(--sky-blue);border-radius:2px}
  .tagline{position:absolute;left:34px;top:154px;font-weight:700;font-size:17px;line-height:1.15;color:#fff}
  .circle-photo{position:absolute;left:237px;top:144px;width:106px;height:106px;border-radius:50%;border:3px solid #fff;
    background:linear-gradient(90deg,#d9d4cc 0%,#cfc5b5 40%,#8b6b4f 50%,#a98462 62%,#cfc6b8 75%,#a8b08a 100%)}
  .local{position:absolute;left:362px;top:206px;font-weight:700;font-size:16.5px;line-height:1.18;color:#fff;padding-right:10px;border-right:1.5px dashed rgba(255,255,255,.8)}
  .years{position:absolute;left:583px;top:198px;font-family:"Oswald",sans-serif;font-weight:700;color:var(--yellow);line-height:1;white-space:nowrap}
  .years-num{font-size:44px}
  .years-word{font-size:29px;color:#fff;margin-left:4px}

  .products-title{position:absolute;left:36px;top:265px;font-weight:800;font-size:13.5px;line-height:1.2;color:var(--navy)}
  .products-title span{color:var(--ink);font-weight:700}
  .products-brand{position:absolute;left:177px;top:281px;font-weight:700;font-size:13.5px;color:var(--ink)}
  .product{position:absolute;width:96px;height:79px;border:2px solid #fff;box-shadow:0 1px 3px rgba(0,0,0,.3);overflow:hidden}
  .product-caption{position:absolute;left:0;bottom:0;width:100%;padding:2px 0;background:rgba(15,74,134,.85);color:#fff;font-weight:600;font-size:7.5px;line-height:1.15;text-align:center}
  .p1{left:36px;top:311px;background:linear-gradient(180deg,#b99571 0%,#8aa3a8 45%,#6f8c5a 100%)}
  .p2{left:142px;top:311px;background:linear-gradient(180deg,#bfc3c6 0%,#e9e9e6 45%,#9aa6ad 100%)}
  .p3{left:36px;top:399px;background:linear-gradient(180deg,#d8d4cc 0%,#ece9e2 50%,#b9a48a 100%)}
  .p4{left:142px;top:399px;background:linear-gradient(180deg,#8fb8e8 0%,#d9c3a4 40%,#3a3b3c 70%,#8fa56f 100%)}

  .offer-band{position:absolute;left:355px;top:272px;width:310px;height:51px;background:var(--yellow)}
  .offer-pct{position:absolute;left:263px;top:262px;font-family:"Oswald",sans-serif;font-weight:700;font-size:58px;line-height:1;color:var(--navy);letter-spacing:-1px}
  .offer-off{position:absolute;left:387px;top:274px;font-weight:800;font-size:19px;color:var(--ink);line-height:1}
  .offer-terms{position:absolute;left:387px;top:296px;font-weight:600;font-size:7.6px;line-height:1.3;color:var(--ink)}
  .warranty-badge{position:absolute;left:620px;top:270px}

  .estimate{position:absolute;left:264px;top:334px;font-size:17px;line-height:1.15;font-weight:500;padding-right:10px;border-right:1.5px dashed var(--rule)}
  .estimate b{font-weight:800}
  .estimate .estimate-cta{display:block;color:var(--navy);font-weight:800}
  .contact{position:absolute;left:400px;top:333px}
  .contact-row{display:flex;align-items:center;gap:9px;height:26px}
  .contact-phone{font-weight:800;font-size:21px}
  .contact-web{font-weight:700;font-size:13.5px}

  .showroom{position:absolute;left:263px;top:393px;width:310px;height:51px;border:1px solid var(--rule);border-radius:4px;background:#fff}
  .showroom-tab{position:absolute;left:-1px;top:-1px;width:216px;height:22px;background:var(--sky-blue);border-radius:4px 0 0 0;clip-path:polygon(0 0,100% 0,90% 100%,0 100%);color:#fff;font-weight:700;font-size:14px;line-height:22px;padding-left:11px}
  .showroom-address{position:absolute;left:12px;top:27px;display:flex;align-items:center;gap:7px;font-weight:700;font-size:12px}
  .hours{position:absolute;left:565px;top:392px;width:149px;height:52px;border-radius:4px;overflow:hidden;text-align:center}
  .hours-days{height:26px;background:var(--navy);color:#fff;font-weight:700;font-size:12.5px;line-height:26px}
  .hours-time{height:26px;background:var(--yellow);color:var(--ink);font-weight:800;font-size:12.5px;line-height:26px}

  .license{position:absolute;left:264px;top:462px;font-weight:700;font-size:10.5px}
  .partners{position:absolute;left:460px;top:458px;display:flex;gap:14px;align-items:center}
  .partner{background:#cfcfcf;border-radius:2px}
  .footer-bar{position:absolute;left:0;bottom:0;width:760px;height:10px;background:var(--navy)}
</style>
</head>
<body>
<main class="ad">
  <section class="hero">
    <div class="hero-photo" role="img" aria-label="Photo of a tan retractable awning shading a desert patio with pool, plants and lounge chairs"></div>
    <div class="hero-fade"></div>
    <svg class="hero-waves" width="760" height="255" viewBox="0 0 760 255" aria-hidden="true">
      <path d="M300 225 Q520 160 760 218 L760 255 L300 255 Z" fill="var(--mid-blue)"/>
      <path d="M300 225 Q520 160 760 218" fill="none" stroke="#fff" stroke-width="1.5"/>
      <path d="M0 222 Q160 245 320 236 L320 255 L0 255 Z" fill="var(--mid-blue)"/>
      <path d="M0 222 Q160 245 320 236" fill="none" stroke="#fff" stroke-width="1.2"/>
    </svg>
    <div class="brand"><span class="brand-dot"></span><span class="brand-name">BRIGHTFOLD</span></div>
    <h1 class="headline">
      <span class="headline-main">BRIGHTFOLD</span>
      <span class="headline-sub">RETRACTABLE SHADES</span>
    </h1>
    <div class="headline-bar"></div>
    <p class="tagline">Save on your custom<br>shade project</p>
    <div class="circle-photo" role="img" aria-label="Photo of a stone column beside a lowered exterior shade"></div>
    <p class="local">Locally Manufactured<br>in Tucson for Over</p>
    <p class="years"><span class="years-num">25</span><span class="years-word">YEARS</span></p>
  </section>

  <h2 class="products-title">MANY PRODUCTS TO<br><span>CHOOSE FROM</span></h2>
  <span class="products-brand">LUMORA</span>
  <figure class="product p1" role="img" aria-label="Photo of a cable-guided shade on a patio"><figcaption class="product-caption">Cable-guided<br>shade</figcaption></figure>
  <figure class="product p2" role="img" aria-label="Photo of a canopy shade"><figcaption class="product-caption">Canopy<br>shade</figcaption></figure>
  <figure class="product p3" role="img" aria-label="Photo of interior retractable shades in a living room"><figcaption class="product-caption">Interior Retractable<br>Shade</figcaption></figure>
  <figure class="product p4" role="img" aria-label="Photo of a solar powered exterior shade"><figcaption class="product-caption">Lumora Solar<br>Powered Shade</figcaption></figure>

  <div class="offer-band"></div>
  <p class="offer-pct">20%</p>
  <p class="offer-off">OFF</p>
  <p class="offer-terms">Some exclusions may apply. Cannot be combined<br>with other offers or discounts. Expires 8/18/22</p>
  <svg class="warranty-badge" width="96" height="96" viewBox="0 0 96 96" aria-label="Lifetime warranty seal" role="img">
    <circle cx="48" cy="48" r="46" fill="var(--sky-blue)"/>
    <circle cx="48" cy="48" r="38" fill="var(--navy)" stroke="#fff" stroke-width="2"/>
  </svg>

  <p class="estimate">GET A <b>FREE</b><span class="estimate-cta">ESTIMATE!</span></p>
  <div class="contact">
    <div class="contact-row">
      <svg width="16" height="16" viewBox="0 0 24 24" aria-hidden="true"><path d="M6.6 10.8a15 15 0 0 0 6.6 6.6l2.2-2.2a1 1 0 0 1 1-.25 11.4 11.4 0 0 0 3.6.57 1 1 0 0 1 1 1V20a1 1 0 0 1-1 1A17 17 0 0 1 3 4a1 1 0 0 1 1-1h3.5a1 1 0 0 1 1 1c0 1.25.2 2.45.57 3.57a1 1 0 0 1-.25 1z" fill="var(--mid-blue)"/></svg>
      <span class="contact-phone">520.555.0187</span>
    </div>
    <div class="contact-row">
      <svg width="16" height="16" viewBox="0 0 24 24" aria-hidden="true"><g fill="none" stroke="var(--mid-blue)" stroke-width="2"><circle cx="12" cy="12" r="9"/><ellipse cx="12" cy="12" rx="4" ry="9"/><path d="M3 12h18M5 7h14M5 17h14"/></g></svg>
      <span class="contact-web">www.brightfoldcovers.example</span>
    </div>
  </div>

  <div class="showroom">
    <div class="showroom-tab">Visit our showroom</div>
    <p class="showroom-address">
      <svg width="10" height="14" viewBox="0 0 10 14" aria-hidden="true"><path d="M5 0a5 5 0 0 0-5 5c0 3.8 5 9 5 9s5-5.2 5-9a5 5 0 0 0-5-5zm0 7a2 2 0 1 1 0-4 2 2 0 0 1 0 4z" fill="var(--mid-blue)"/></svg>
      473 W. Pellham Rd | Tucson, AZ 85790
    </p>
  </div>
  <div class="hours">
    <div class="hours-days">MONDAY - FRIDAY</div>
    <div class="hours-time">10AM - 4PM</div>
  </div>

  <p class="license">Bonded • Insured ROC# CR-904317</p>
  <div class="partners" aria-label="Partner and accreditation badges">
    <span class="partner" style="width:62px;height:16px"></span>
    <span class="partner" style="width:56px;height:16px"></span>
    <span class="partner" style="width:36px;height:18px"></span>
    <span class="partner" style="width:18px;height:22px"></span>
  </div>
  <div class="footer-bar"></div>
</main>
</body>
</html>
```